Business Card Design Project

Need business card for new non profit organization that includes the attached logo in some form.
with this information
Name: Martin Holloway Pryce
Title: President & Founder
A: P.O. Box 51637, Portland, Oregon, 97209-1637
E: marty@hollowayfoundation.org
E: marty@martypryce.com
P: 1.971.555.0172

```html
<!DOCTYPE html>
<html lang="en">
<head>
<meta charset="utf-8">
<title>Holloway Foundation – Business Card</title>
<link rel="stylesheet" href="https://fonts.googleapis.com/css2?family=Tinos:wght@400;700&display=swap">
<style>
  :root {
    --paper: #f9f6f7;
    --navy: #0b2a6c;
    --navy-deep: #06225f;
    --band-edge: #8f96a6;
    --band-light: #c9d1e3;
    --ink-light: #ffffff;
  }
  * { margin: 0; padding: 0; box-sizing: border-box; }
  html, body {
    width: 1200px;
    height: 752px;
    overflow: hidden;
    background: var(--paper);
  }
  .card {
    position: relative;
    width: 1200px;
    height: 752px;
    background: var(--paper);
    font-family: "Tinos", "Times New Roman", serif;
    color: var(--navy);
    text-align: center;
  }
  .card p, .card h1 {
    position: absolute;
    left: 0;
    right: 0;
    line-height: 1;
    white-space: nowrap;
  }
  .brand-mark {
    position: absolute;
    left: 520px;
    top: 58px;
    width: 160px;
    height: 160px;
  }
  .org-name {
    top: 221px;
    font-size: 72px;
    font-weight: 700;
    color: var(--navy);
  }
  .person-name {
    top: 350px;
    font-size: 38px;
    font-weight: 400;
    letter-spacing: 0.5px;
    text-transform: uppercase;
  }
  .person-title {
    top: 394px;
    font-size: 40px;
  }
  .divider {
    position: absolute;
    left: 0;
    top: 450px;
    width: 1200px;
    height: 16px;
    background: linear-gradient(90deg, var(--band-edge) 0%, var(--band-light) 50%, var(--band-edge) 100%);
  }
  .contact-panel {
    position: absolute;
    left: 0;
    top: 466px;
    width: 1200px;
    height: 286px;
    background: var(--navy-deep);
  }
  .contact-line { color: var(--ink-light); }
  .address { top: 487px; font-size: 41px; }
  .email-org { top: 541px; font-size: 39px; }
  .email-personal { top: 587px; font-size: 39px; }
  .phone { top: 642px; font-size: 39px; }
</style>
</head>
<body>
  <div class="card">
    <svg class="brand-mark" viewBox="0 0 160 160" aria-hidden="true">
      <circle cx="80" cy="80" r="78" fill="#0b2a6c"/>
    </svg>
    <h1 class="org-name">Holloway Foundation</h1>

    <p class="person-name">Martin Holloway Pryce</p>
    <p class="person-title">President &amp; Founder</p>

    <div class="divider"></div>
    <div class="contact-panel"></div>

    <p class="contact-line address">P.O. Box 51637, Portland, Oregon, 97209-1637</p>
    <p class="contact-line email-org">marty@hollowayfoundation.org</p>
    <p class="contact-line email-personal">marty@martypryce.com</p>
    <p class="contact-line phone">1.971.555.0172</p>
  </div>
</body>
</html>
```